BrewHaunt coffee packaging design

We need a vector design (AI) for the printing of our coffee bags.

The bags are double sided. Front will be simple with logo and web address. Back will have lots of information (below) and the wording can be changed to suit if required.

Actual bag dimensions are: 240mm wide x 335mm high (each side) artwork should be inside those sizes.

Front:
Requires - BrewHaunt cup logo, web address (brewhaunt.com.au) in lowercase Papyrus font and the words BREW HAUNT in uppercase.
**added** The front will also need a 90mm x 35mm no artwork area so we can place a sticker.

Back:
1.
Velvet Kettle Logo (needs to be entire unmodified logo) and the tagline of "Overall winner of Australia's biggest coffee roasting competition"

2.
BrewHaunt is a family business, proudly Australian owned and operated. We strive to provide amazing coffee, excellent service and great value to all our customers.

3.
Our coffee is fresh roasted to order and shipped same day.

4.
50c from every kilogram sold goes directly to projects in coffee growing regions. TrueLoop is the Fairest Trade of all - see: trueloop.net

Logos are attached and higher resolution ones are available if needed.

Requirements
Must have
• Per the description, BrewHaunt logo and webaddress on the front and Velvet Kettle logo on the back are required.

```html
<!DOCTYPE html>
<html lang="en">
<head>
<meta charset="utf-8">
<title>BrewHaunt coffee bag – front and back</title>
<link rel="stylesheet" href="https://fonts.googleapis.com/css2?family=Cinzel:wght@400;700&family=Macondo&family=Italianno&display=swap">
<style>
  :root {
    --page: #f1efec;
    --roast: #2b1a12;
    --roast-deep: #1c100a;
    --bean-light: #6b4426;
    --bean-dark: #2a170c;
    --gold: #c9a24a;
    --gold-soft: #e2c47a;
    --cream: #f6efe2;
    --sticker: #ffffff;
    --ink: #3a2416;
  }
  * { box-sizing: border-box; margin: 0; padding: 0; }
  html, body { width: 885px; height: 1200px; overflow: hidden; background: var(--page); }
  .sheet {
    position: relative; width: 885px; height: 1200px;
    display: flex; justify-content: center; align-items: center; gap: 40px;
  }
  .bag-side {
    position: relative; width: 400px; height: 558px; overflow: hidden;
    box-shadow: 0 2px 10px rgba(0,0,0,.18);
  }

  /* Front */
  .bag-front { background: var(--roast); }
  .bean-field {
    position: absolute; inset: 0;
  }
  .brand-title {
    position: absolute; left: 28px; top: 64px; width: 180px;
    font-family: "Cinzel", serif; color: var(--gold);
    font-size: 40px; line-height: 1.02; letter-spacing: 1px; text-align: center;
  }
  .sticker-area {
    position: absolute; left: 28px; top: 168px; width: 150px; height: 58px;
    background: var(--sticker);
    font-family: "Cinzel", serif; font-size: 11px; color: var(--ink);
    padding: 8px 10px;
  }
  .front-mark {
    position: absolute; left: 26px; top: 380px; width: 180px;
    display: flex; align-items: center; gap: 10px;
    font-family: "Cinzel", serif; font-weight: 700; font-size: 24px; color: var(--gold);
  }
  .front-mark .dot { width: 26px; height: 26px; border-radius: 50%; background: var(--gold); flex: none; }
  .web-address {
    position: absolute; left: 28px; top: 505px; width: 180px; text-align: center;
    font-family: "Macondo", cursive; font-size: 15px; color: var(--gold-soft);
  }

  /* Back */
  .bag-back { background: var(--cream); }
  .award-mark {
    position: absolute; left: 22px; top: 52px; width: 150px;
    display: flex; align-items: center; gap: 8px;
    font-family: "Macondo", cursive; font-size: 20px; color: var(--ink);
  }
  .award-mark .dot { width: 22px; height: 22px; border-radius: 50%; background: var(--gold); flex: none; }
  .award-tagline {
    position: absolute; right: 20px; top: 26px; width: 190px; text-align: center;
    font-family: "Italianno", cursive; font-size: 27px; line-height: .95; color: var(--ink);
  }
  .info-panel { position: absolute; left: 0; top: 0; width: 400px; height: 558px; }
  .info-copy {
    position: absolute; left: 48px; right: 48px; top: 222px;
    font-family: "Macondo", cursive; font-size: 14.5px; line-height: 1.3;
    color: var(--cream); text-align: center;
  }
  .info-copy p + p { margin-top: 22px; }
</style>
</head>
<body>
<main class="sheet">

  <section class="bag-side bag-front" aria-label="Bag front">
    <svg class="bean-field" width="400" height="558" viewBox="0 0 400 558" role="img" aria-label="Field of roasted coffee beans down the right side of the bag">
      <defs>
        <linearGradient id="beanTone" x1="0" y1="0" x2="1" y2="1">
          <stop offset="0" stop-color="var(--bean-dark)"/>
          <stop offset=".5" stop-color="var(--bean-light)"/>
          <stop offset="1" stop-color="var(--bean-dark)"/>
        </linearGradient>
      </defs>
      <path d="M250 0 C215 90 300 170 255 260 C215 350 300 440 245 558 L400 558 L400 0 Z" fill="url(#beanTone)"/>
    </svg>
    <h1 class="brand-title">BREW<br>HAUNT</h1>
    <div class="sticker-area">STICKER</div>
    <div class="front-mark"><span class="dot"></span>BrewHaunt</div>
    <p class="web-address">brewhaunt.com.au</p>
  </section>

  <section class="bag-side bag-back" aria-label="Bag back">
    <svg class="info-panel" width="400" height="558" viewBox="0 0 400 558" aria-hidden="true">
      <path d="M0 188 C120 150 260 200 400 140 L400 558 L0 558 Z" fill="var(--roast)"/>
      <path d="M0 188 C120 150 260 200 400 140" fill="none" stroke="var(--gold)" stroke-width="2"/>
    </svg>
    <div class="award-mark"><span class="dot"></span>Velvet Kettle</div>
    <p class="award-tagline">Overall winner of Australia's biggest coffee roasting competition</p>
    <div class="info-copy">
      <p>BrewHaunt is a family business, proudly Australian owned and operated. We strive to provide amazing coffee, excellent service and great value to all our customers.</p>
      <p>Our coffee is fresh roasted to order and shipped same day.</p>
      <p>50c from every kilogram sold goes directly to projects in coffee growing regions. TrueLoop is the Fairest Trade of all – see: trueloop.net</p>
    </div>
  </section>

</main>
</body>
</html>
```